TalkBloom - Language Coaching Services

Sleek, innovative, trendy design for Language Coaching business.

TalkBloom is a new UK based company that provides Language Coaching services. We offer highly personalized on-line and face to face language courses. We also impart learning techniques workshops based on the latest neuroscience research for second-language acquisition.

Target Market(s)

Industry/Entity Type

Consulting

Contact Information for Business Card

TalkBloom
DaniraQT@talkbloom.co.uk
TalkBloom.co.uk
London, UK

Font styles to use
Sans Serif

```html
<!DOCTYPE html>
<html lang="en">
<head>
<meta charset="utf-8">
<title>TalkBloom Business Card</title>
<link href="https://fonts.googleapis.com/css2?family=Open+Sans:wght@400;600;700&display=swap" rel="stylesheet">
<style>
  :root {
    --stage: #4a423d;
    --card-dark: #1c1f23;
    --card-light: #ffffff;
    --silver: #d6d8da;
    --brand-blue: #1b8fc9;
    --deep-blue: #1e5d8c;
    --ink-grey: #555a60;
    --divider: #a9acaf;
  }
  * { box-sizing: border-box; margin: 0; padding: 0; }
  html, body { width: 1200px; height: 864px; overflow: hidden; }
  body {
    background: var(--stage);
    font-family: "Open Sans", sans-serif;
    position: relative;
  }
  .card {
    position: absolute;
    width: 520px;
    height: 298px;
    border-radius: 3px;
    box-shadow: 0 8px 24px rgba(0,0,0,.35);
  }
  .card-front {
    left: 60px; top: 110px;
    background: var(--card-dark);
  }
  .card-back {
    left: 620px; top: 456px;
    background: var(--card-light);
  }
  .brand {
    position: absolute;
    display: flex;
    align-items: center;
    gap: 14px;
  }
  .brand-dot {
    width: 58px; height: 58px;
    border-radius: 50%;
    border: 5px solid currentColor;
  }
  .brand-name {
    font-weight: 600;
    font-size: 40px;
    letter-spacing: 1px;
  }
  .card-front .brand {
    color: var(--silver);
    left: 108px; top: 90px;
  }
  .front-url {
    position: absolute;
    left: 0; right: 0; top: 190px;
    text-align: center;
    color: var(--silver);
    font-size: 14px;
    letter-spacing: 5px;
  }
  .card-back .brand {
    color: var(--brand-blue);
    left: 28px; top: 118px;
  }
  .card-back .brand-dot { width: 46px; height: 46px; border-width: 4px; }
  .card-back .brand-name { font-size: 30px; }
  .divider {
    position: absolute;
    left: 292px; top: 70px;
    width: 1px; height: 158px;
    background: linear-gradient(to bottom, transparent, var(--divider) 25%, var(--divider) 75%, transparent);
  }
  .contact {
    position: absolute;
    left: 318px; top: 92px;
  }
  .person-name {
    color: var(--deep-blue);
    font-weight: 700;
    font-size: 20px;
    line-height: 1;
  }
  .person-role {
    color: #8d9196;
    font-size: 13px;
    letter-spacing: .5px;
    margin-bottom: 12px;
  }
  .contact-list { list-style: none; }
  .contact-list li {
    display: flex;
    align-items: center;
    gap: 8px;
    color: var(--ink-grey);
    font-size: 13.5px;
    line-height: 22px;
  }
  .contact-list svg { width: 13px; height: 13px; fill: var(--deep-blue); flex: none; }
</style>
</head>
<body>
  <section class="card card-front">
    <div class="brand">
      <span class="brand-dot"></span>
      <span class="brand-name">TalkBloom</span>
    </div>
    <p class="front-url">www.talkbloom.co.uk</p>
  </section>

  <section class="card card-back">
    <div class="brand">
      <span class="brand-dot"></span>
      <span class="brand-name">TalkBloom</span>
    </div>
    <div class="divider"></div>
    <div class="contact">
      <p class="person-name">ALAN REID</p>
      <p class="person-role">PRESIDENT</p>
      <ul class="contact-list">
        <li>
          <svg viewBox="0 0 12 12"><path d="M3 0h6a1 1 0 0 1 1 1v10a1 1 0 0 1-1 1H3a1 1 0 0 1-1-1V1a1 1 0 0 1 1-1zm.5 1.5v8h5v-8zM6 10.2a.6.6 0 1 0 0 1.2.6.6 0 0 0 0-1.2z"/></svg>
          555 0142 7781
        </li>
        <li>
          <svg viewBox="0 0 12 12"><path d="M0 2h12v8H0zm1 1v.3l5 3.2 5-3.2V3zm0 1.5V9h10V4.5L6 7.7z"/></svg>
          info@talkbloom.co.uk
        </li>
        <li>
          <svg viewBox="0 0 12 12"><circle cx="6" cy="6" r="6"/><path d="M3 4h6M3 8h6M6 0v12" stroke="#fff" stroke-width=".8" fill="none"/></svg>
          talkbloom.co.uk
        </li>
      </ul>
    </div>
  </section>
</body>
</html>
```